Tavik Sales Pipeline

We need an infographic to help the sales team understand the importance of a sales pipeline and how to grow and manage it. It's important that they understand every process plays a vital part and a complete circle. If you break one part, the sales process can be a failure.

Target Market(s)

Infographic Designer

Font styles to use
Serif

Colors
33b8a4
abd037

Requirements
Must have
• Have fun!
Nice to have
• Open to all ideas. Keep in mind that we are eastern philosophy focused!
Should not have
• Not applicable! Just have phone

```html
<!DOCTYPE html>
<html lang="en">
<head>
<meta charset="utf-8">
<title>Tavik Sales Pipeline</title>
<link rel="stylesheet" href="https://fonts.googleapis.com/css2?family=Raleway:wght@500;700;800&display=swap">
<style>
  :root {
    --teal: #24b9a3;
    --teal-text: #26b3a0;
    --green: #abd037;
    --green-light: #b5d646;
    --panel-left: #f1f3f2;
    --panel-right: #ebebeb;
    --ring: #e2e3e3;
    --ink: #5a5a5a;
    --ink-strong: #4f4f4f;
    --label: #6b6b6b;
    --white: #ffffff;
  }
  * { margin: 0; padding: 0; box-sizing: border-box; }
  html, body { width: 1200px; height: 726px; overflow: hidden; }
  body { font-family: "Raleway", sans-serif; color: var(--ink); }
  .infographic { position: relative; width: 1200px; height: 726px; background: var(--panel-right); }
  .diagram-panel { position: absolute; left: 0; top: 0; width: 630px; height: 726px; background: var(--panel-left); }
  .title-pill {
    position: absolute; left: 138px; top: 36px; width: 349px; height: 59px; border-radius: 30px;
    background: linear-gradient(90deg, var(--green), var(--green-light));
    display: flex; align-items: center; justify-content: center;
    color: var(--white); font-weight: 800; font-size: 34px; letter-spacing: 0.3px;
  }
  .pipeline-diagram { position: absolute; left: 0; top: 0; width: 630px; height: 726px; }
  .stage-label { font-family: "Raleway", sans-serif; font-weight: 700; font-size: 21px; fill: var(--label); text-anchor: middle; }
  .stage-number { font-family: "Raleway", sans-serif; font-weight: 800; font-size: 50px; fill: var(--white); text-anchor: middle; }
  .flow-label { font-family: "Raleway", sans-serif; font-weight: 700; font-size: 25px; fill: var(--teal-text); }
  .source-label { font-family: "Raleway", sans-serif; font-weight: 700; font-size: 21px; fill: var(--teal-text); }

  .summary { position: absolute; left: 694px; top: 0; width: 480px; }
  .summary-marker { position: absolute; left: 0; top: 178px; width: 0; height: 0;
    border-top: 22px solid transparent; border-bottom: 22px solid transparent; border-right: 28px solid var(--green); }
  .summary-intro { position: absolute; left: 50px; top: 170px; font-size: 22px; line-height: 29px; font-weight: 500; color: var(--ink); width: 420px; }
  .summary-intro strong { font-weight: 700; color: var(--ink-strong); }
  .focus-heading { position: absolute; left: 50px; top: 301px; font-size: 18px; font-weight: 700; color: var(--ink-strong); }
  .focus-list { position: absolute; left: 50px; top: 362px; list-style: none; }
  .focus-list li { font-size: 18px; font-weight: 500; height: 51px; color: var(--ink); }
  .focus-list .focus-number { color: var(--green); font-weight: 800; }
</style>
</head>
<body>
<main class="infographic">
  <section class="diagram-panel">
    <h1 class="title-pill">TAVIK Pipeline</h1>
    <svg class="pipeline-diagram" viewBox="0 0 815 939" role="img" aria-label="Five-stage circular sales pipeline">
      <g class="stage-rings" fill="var(--panel-left)" stroke="var(--ring)" stroke-width="11">
        <circle cx="400" cy="285" r="100"/>
        <circle cx="178" cy="440" r="100"/>
        <circle cx="622" cy="440" r="100"/>
        <circle cx="262" cy="693" r="100"/>
        <circle cx="536" cy="693" r="100"/>
      </g>
      <g class="flow-band" stroke="var(--teal)" stroke-width="40" fill="none" stroke-linejoin="round">
        <polygon points="290,650 230,460 398,335 570,460 503,650"/>
      </g>
      <g class="flow-band-shade" stroke="#1f9f8c" stroke-width="14" fill="none" opacity="0.45" stroke-linejoin="round">
        <polygon points="298,640 245,468 398,355 555,468 497,640"/>
      </g>
      <g class="flow-chevrons" stroke="var(--panel-left)" stroke-width="10" fill="none" stroke-linejoin="miter">
        <polyline points="286.8,557 257,545.5 239.2,572"/>
        <polyline points="321,423.5 322,391.5 291,383.5"/>
        <polyline points="461.1,411.9 492.1,403.4 490.7,371.3"/>
        <polyline points="563.3,553.9 533.2,564.4 516.3,537.3"/>
        <polyline points="406.5,675 386.5,650 406.5,625"/>
      </g>
      <g class="stage-leaves" fill="var(--green)">
        <path transform="translate(398,335)" d="M-72,0 Q0,-70 72,0 Q0,70 -72,0Z"/>
        <path transform="translate(230,460) rotate(-72)" d="M-72,0 Q0,-70 72,0 Q0,70 -72,0Z"/>
        <path transform="translate(570,460) rotate(72)" d="M-72,0 Q0,-70 72,0 Q0,70 -72,0Z"/>
        <path transform="translate(290,650) rotate(-36)" d="M-72,0 Q0,-70 72,0 Q0,70 -72,0Z"/>
        <path transform="translate(503,650) rotate(36)" d="M-72,0 Q0,-70 72,0 Q0,70 -72,0Z"/>
      </g>
      <g class="stage-numbers">
        <text class="stage-number" x="398" y="355">3</text>
        <text class="stage-number" x="230" y="480">2</text>
        <text class="stage-number" x="572" y="480">4</text>
        <text class="stage-number" x="291" y="675">1</text>
        <text class="stage-number" x="503" y="675">5</text>
      </g>
      <g class="stage-labels">
        <text class="stage-label" x="400" y="262">Engagement</text>
        <text class="stage-label" x="400" y="285">Cycle</text>
        <text class="stage-label" x="146" y="431">Nurture</text>
        <text class="stage-label" x="146" y="454">Rapport</text>
        <text class="stage-label" x="655" y="431" style="font-size:24px">Peak</text>
        <text class="stage-label" x="652" y="454" style="font-size:24px">Cycle</text>
        <text class="stage-label" x="259" y="721">Collection</text>
        <text class="stage-label" x="259" y="751">Build-up</text>
        <text class="stage-label" x="535" y="722" style="font-size:23px">Retention</text>
      </g>
      <g class="flow-labels">
        <text class="flow-label" x="183" y="305">Harvest</text>
        <text class="flow-label" x="520" y="290">Package/</text>
        <text class="flow-label" x="520" y="324">Present</text>
        <text class="flow-label" x="38" y="592">Water/Sun</text>
        <text class="flow-label" x="629" y="592">Closure</text>
        <text class="flow-label" x="373" y="772">Seed/</text>
        <text class="flow-label" x="373" y="806">Plant</text>
      </g>
      <g class="lead-sources">
        <path d="M398,868 H314 L300,808" fill="none" stroke="var(--teal)" stroke-width="12" stroke-linejoin="round" stroke-linecap="round"/>
        <polygon points="283,810 296,780 318,806" fill="var(--teal)"/>
        <text class="source-label" x="418" y="875">Lead Sources</text>
      </g>
    </svg>
  </section>

  <section class="summary">
    <span class="summary-marker"></span>
    <p class="summary-intro"><strong>TAVIK Sales Pipeline</strong> focuses on the understanding of the Subject Life Cycle</p>
    <h2 class="focus-heading">Mastering Five Key Focuses:</h2>
    <ol class="focus-list">
      <li><span class="focus-number">1.</span> Collection/Build-up (Seed)</li>
      <li><span class="focus-number">2.</span> Nurture/Rapport (Water/Sun)</li>
      <li><span class="focus-number">3.</span> Engagement (Harvest/Prune)</li>
      <li><span class="focus-number">4.</span> Peak/Summit (Package/Presentation)</li>
      <li><span class="focus-number">5.</span> Retention/Descent (Plant)</li>
    </ol>
  </section>
</main>
</body>
</html>
```